Business Card for Quillmark Ledger - A cannabis publication for executives.

I'd like some business cards for Quillmark Ledger. The logo is done (great job!) and I need a card design I will use with PRINTLY. I made it a short project to allow time for printing before an event. These will be standard sized cards (final artwork size 3.66" x 2.16" at 300dpi) with a final card size of 3.5" x 2.0". (See PRINTLY.com if you need more info.) I might try rounded corners but am not sure yet. I think the design will work okay with rounded.

Quillmark Ledger will be a bi-weekly publication for the cannabis industry. It is targeted to investors and industry executives, not consumers or pot smokers. So our market is more B2B. However I am open to creativity and making the card something people remark on.

My contact for card:

Dana Merrow
Founder/CEO
dana@quillmarkledger.example

2740 Harlow Avenue
Boston MA 02135
(617)555-0194

Target Market(s)

Executives, Industry people and investors in the Cannabis sector.

Contact Information for Business Card

PRINTLY does do double sided and the second side can be the same or different images. Only one side is required but use of the second side would be a bonus.

Font styles to use
Serif
Sans Serif
Decorative

Colors

Designer to choose colors to be used in the design.

Requirements
Must have
• Logo, contact info
Nice to have
• Style and design to make the card stand out in a crowd.

```html
<!DOCTYPE html>
<html lang="en">
<head>
<meta charset="utf-8">
<title>Quillmark Ledger – Business Card</title>
<link rel="stylesheet" href="https://fonts.googleapis.com/css2?family=Fira+Sans:wght@400;600&family=Fira+Sans+Condensed:wght@600&display=swap">
<style>
  :root {
    --bg: #e6e7e9;
    --card: #ffffff;
    --blue: #1b72c0;
    --green: #6db33f;
    --ink: #3a3a3a;
    --muted: #555a60;
  }
  * { margin: 0; padding: 0; box-sizing: border-box; }
  html, body { width: 1200px; height: 1200px; overflow: hidden; }
  body {
    background: var(--bg);
    font-family: "Fira Sans", Arial, sans-serif;
    color: var(--ink);
    position: relative;
  }
  .card {
    position: absolute;
    left: 180px;
    width: 840px;
    height: 480px;
    background: var(--card);
    box-shadow: 0 2px 10px rgba(0,0,0,0.12);
  }
  .card--front { top: 90px; }
  .card--back  { top: 630px; display: flex; align-items: center; justify-content: center; }

  .wordmark {
    display: flex;
    align-items: center;
    gap: 16px;
  }
  .wordmark__square {
    width: 40px; height: 40px;
    background: var(--green);
    flex: none;
  }
  .wordmark__name {
    font-family: "Fira Sans", Arial, sans-serif;
    font-weight: 600;
    color: var(--blue);
    font-size: 40px;
    letter-spacing: -0.5px;
    white-space: nowrap;
  }
  .card--front .wordmark { position: absolute; left: 60px; top: 48px; }
  .card--back .wordmark__square { width: 58px; height: 58px; }
  .card--back .wordmark__name { font-size: 60px; }

  .person { position: absolute; left: 60px; top: 140px; }
  .person__name {
    font-family: "Fira Sans Condensed", "Arial Narrow", sans-serif;
    font-weight: 600;
    font-size: 36px;
    color: var(--blue);
    text-transform: uppercase;
    letter-spacing: -0.5px;
  }
  .person__title { font-size: 20px; color: var(--muted); margin-top: 2px; }

  .divider {
    position: absolute;
    left: 60px; right: 60px; top: 262px;
    height: 1.5px;
    background: var(--green);
  }

  .address {
    position: absolute;
    right: 60px; top: 178px;
    display: flex; gap: 10px;
    font-size: 20px; line-height: 1.3; color: var(--ink);
  }
  .contact {
    position: absolute;
    left: 60px; top: 288px;
    font-size: 19px; line-height: 1.5; color: var(--ink);
  }
  .contact__row, .address { align-items: flex-start; }
  .contact__row { display: flex; align-items: center; gap: 10px; }
  .icon { width: 18px; height: 18px; flex: none; }
  .address .icon { margin-top: 4px; }
</style>
</head>
<body>
  <section class="card card--front" aria-label="Business card front">
    <div class="wordmark">
      <span class="wordmark__square"></span>
      <span class="wordmark__name">Quillmark Ledger</span>
    </div>

    <div class="person">
      <p class="person__name">Dana Merrow</p>
      <p class="person__title">Founder/CEO</p>
    </div>

    <div class="address">
      <svg class="icon" viewBox="0 0 18 18" aria-hidden="true">
        <path d="M9 1a6 6 0 0 0-6 6c0 4.5 6 10 6 10s6-5.5 6-10a6 6 0 0 0-6-6z" fill="var(--blue)"/>
        <circle cx="9" cy="7" r="2.2" fill="#fff"/>
      </svg>
      <p>2740 Harlow Avenue<br>Boston MA 02135</p>
    </div>

    <div class="divider"></div>

    <div class="contact">
      <p class="contact__row">
        <svg class="icon" viewBox="0 0 18 18" aria-hidden="true">
          <path d="M3 7c0-2 2.5-3.5 6-3.5S15 5 15 7l-2.5.8L11.5 6h-5L5.5 7.8z" fill="var(--blue)"/>
          <rect x="3.5" y="9" width="11" height="6" rx="1" fill="none" stroke="var(--blue)" stroke-width="1.6"/>
        </svg>
        (617)555-0194
      </p>
      <p class="contact__row">
        <svg class="icon" viewBox="0 0 18 18" aria-hidden="true">
          <rect x="1.5" y="3.5" width="15" height="11" fill="var(--blue)"/>
          <path d="M1.5 3.5l7.5 6 7.5-6M1.5 14.5l5.5-5M16.5 14.5l-5.5-5" fill="none" stroke="#fff" stroke-width="1.2"/>
        </svg>
        dana@quillmarkledger.example
      </p>
    </div>
  </section>

  <section class="card card--back" aria-label="Business card back">
    <div class="wordmark">
      <span class="wordmark__square"></span>
      <span class="wordmark__name">Quillmark Ledger</span>
    </div>
  </section>
</body>
</html>
```